Trade Show Booth Back Wall Graphic (20 feet x 8 feet)

Design a bold 20x8 illuminated trade show booth wall that incorporates our logo, plus important text describing our product and services. In an ocean of trade show booths, it must stand out. Overly complicated or busy designs may not be effective. Your design should capture the eye instantly while walking by, but be clean and clear enough to explain what the company does in 5 seconds, making people want to look closer. INCLUDED TEXT AND DIRECTIONS:- The bottom 3 feet on the left half may NOT contain text as seating will be placed in front of that portion, blocking part of the view- "Past Every Horizon, Past Every Limit" is a tag line to be included near our logo. It must have a small TM for trademark. - Flerbo logo must display a small ® for registered trademark- "Bonded 3G/4G Command/Control/Streaming"- " Prioritized Data Service - " Carrier Agnostic - use multiple networks simultaneously"- "600+ Global Cellular Networks Available "

Target Market(s)

This overview explains a key target market: https://www.clipvista-example.com/watch?v=Qz3RkT8pLmW DO NOT INCLUDE DRONE PICTURES IN GRAPHICS. It looks cheap.

Colors
6b449b
abd037

Requirements
Must have
• - Bold, clean, futuristic design incorporating our logo
• - Eye catching and easy to understand at 10' distance AND 75' distance
Nice to have
• This is a backlit wall, so a design that makes our logo and key data points "pop" is desirable
Should not have
• NO PICTURES OF DRONES! Although this is a command and control link for drones, we want to convey that idea WITHOUT using drones in the graphics. Only background graphics in the lower 3-feet of design. There will be lounge chairs placed in front of this wall.

```html
<!DOCTYPE html>
<html lang="en">
<head>
<meta charset="utf-8">
<title>Flerbo Booth Wall</title>
<link rel="stylesheet" href="https://fonts.googleapis.com/css2?family=Arimo:wght@400;700&display=swap">
<style>
  :root {
    --cream: #fdfcf1;
    --purple-light: #6c0f90;
    --purple-dark: #3a0a48;
    --brand-purple: #4b1187;
    --brand-green: #4fbf2a;
    --white: #fffdf3;
    --mark: #9a9a9a;
  }
  html, body {
    margin: 0;
    padding: 0;
    overflow: hidden;
  }
  .wall {
    position: relative;
    width: 1200px;
    height: 480px;
    overflow: hidden;
    font-family: "Arimo", Arial, sans-serif;
    background: var(--cream);
  }
  .brand-panel {
    position: absolute;
    left: 0;
    top: 0;
    width: 368px;
    height: 480px;
    background: var(--cream);
  }
  .brand-name {
    position: absolute;
    left: 94px;
    top: 34px;
    margin: 0;
    font-size: 44px;
    font-weight: 700;
    color: var(--brand-purple);
    letter-spacing: -1px;
    line-height: 1;
  }
  .brand-name sup {
    font-size: 8px;
    vertical-align: baseline;
    position: relative;
    top: 2px;
    margin-left: 3px;
  }
  .tagline {
    position: absolute;
    left: 94px;
    top: 90px;
    margin: 0;
    font-size: 8.5px;
    font-weight: 700;
    color: var(--brand-green);
    white-space: nowrap;
  }
  .tagline sup {
    font-size: 6px;
    vertical-align: top;
    margin-left: 2px;
  }
  .crop-marks {
    position: absolute;
    left: 0;
    top: 0;
  }
  .message-panel {
    position: absolute;
    left: 368px;
    top: 0;
    width: 832px;
    height: 480px;
    background: linear-gradient(160deg, var(--purple-light) 0%, #5a0d7a 45%, var(--purple-dark) 100%);
    box-shadow: inset 14px 0 16px -10px rgba(20, 0, 30, 0.7);
  }
  .headline {
    position: absolute;
    right: 22px;
    top: -28px;
    margin: 0;
    font-size: 262px;
    font-weight: 700;
    line-height: 1;
    letter-spacing: -11px;
    color: var(--white);
    white-space: nowrap;
  }
  .subhead {
    position: absolute;
    right: 24px;
    top: 232px;
    margin: 0;
    font-size: 70px;
    font-weight: 700;
    line-height: 1;
    letter-spacing: -1.5px;
    color: var(--white);
    white-space: nowrap;
  }
  .features {
    position: absolute;
    right: 24px;
    top: 366px;
    margin: 0;
    padding: 0;
    list-style: none;
    text-align: right;
    color: var(--white);
    font-size: 15.5px;
    line-height: 20.8px;
    font-weight: 400;
  }
</style>
</head>
<body>
  <main class="wall">
    <section class="brand-panel">
      <h1 class="brand-name">Flerbo<sup>®</sup></h1>
      <p class="tagline">"Past Every Horizon, Past Every Limit"<sup>™</sup></p>
      <svg class="crop-marks" width="368" height="200" viewBox="0 0 368 200" aria-hidden="true">
        <path d="M53 183 H58 V189" fill="none" stroke="var(--mark)" stroke-width="0.8"/>
        <path d="M315 183 H310 V189" fill="none" stroke="var(--mark)" stroke-width="0.8"/>
      </svg>
    </section>

    <section class="message-panel">
      <h2 class="headline">PSST!</h2>
      <p class="subhead">COME CLOSER</p>
      <ul class="features">
        <li>"Bonded 3G/4G Command/Control/Streaming"</li>
        <li>"Prioritized Data Service"</li>
        <li>"Carrier Agnostic - use multiple networks simultaneously"</li>
        <li>"600+ Global Cellular Networks Available"</li>
      </ul>
    </section>
  </main>
</body>
</html>
```